Independent Financial Advisor Billboard Campaign - Granite Bridge Financial

I am a local, independent financial advisor. My company is Granite Bridge Financial, located in Charleston, WV. My main source of revenue comes from those nearing or entering retirement that need assistance with financial planning and investment management. Many are looking to rollover their employer retirement plan into an IRA account. I would like a billboard design campaign that focuses on this type of client. Please see our website www.granitebridgefinancial-example.com for more information.

```html
<!DOCTYPE html>
<html lang="en">
<head>
<meta charset="utf-8">
<title>Granite Bridge Financial – Billboard</title>
<link href="https://fonts.googleapis.com/css2?family=Raleway:wght@500;600;700;800&display=swap" rel="stylesheet">
<style>
  :root {
    --navy: #1b3a6f;
    --navy-deep: #132c57;
    --slate: #4d4f53;
    --grey-wedge: #6b6c6e;
    --green: #8dc63f;
    --white: #ffffff;
    --page: #e6e6e6;
    --brick: #a0603c;
    --brick-light: #c98a5e;
  }
  * { box-sizing: border-box; margin: 0; padding: 0; }
  html, body {
    width: 1200px; height: 1036px; overflow: hidden;
    background: var(--page);
    font-family: "Raleway", Arial, sans-serif;
  }
  .billboard {
    position: absolute; left: 40px; top: 355px;
    width: 1120px; height: 326px;
    background: var(--white);
    overflow: hidden;
  }
  .billboard-art { position: absolute; inset: 0; width: 100%; height: 100%; }
  .brand {
    position: absolute; left: 57px; top: 24px;
    display: flex; align-items: center; gap: 10px;
  }
  .brand-square { width: 34px; height: 34px; background: var(--navy); }
  .brand-name {
    font-size: 24px; font-weight: 700; color: var(--navy);
    letter-spacing: 0.5px;
  }
  .headline {
    position: absolute; left: 55px; top: 88px;
    font-size: 44px; font-weight: 700; line-height: 43px;
    color: var(--navy);
  }
  .headline-rule {
    position: absolute; left: 55px; top: 194px;
    width: 54px; height: 3px; background: var(--green);
  }
  .services {
    position: absolute; left: 55px; top: 216px;
    display: flex; list-style: none;
  }
  .services li {
    font-size: 17px; font-weight: 600; line-height: 18px;
    color: var(--slate); text-transform: uppercase;
    padding: 0 16px; border-left: 2px solid var(--slate);
  }
  .services li:first-child { padding-left: 0; border-left: none; }
  .contact {
    position: absolute; left: 55px; top: 272px;
    display: flex; align-items: center; height: 40px;
  }
  .phone {
    display: flex; align-items: center; gap: 6px;
    font-size: 30px; font-weight: 800; color: var(--navy);
  }
  .phone svg { width: 22px; height: 22px; }
  .web {
    margin-left: 14px; height: 40px; padding: 0 12px;
    background: var(--navy); display: flex; align-items: center;
    font-size: 16px; font-weight: 500; color: var(--green);
  }
  .web .domain { color: var(--white); }
</style>
</head>
<body>
  <section class="billboard" aria-label="Granite Bridge Financial billboard">
    <svg class="billboard-art" viewBox="0 0 1760 512" preserveAspectRatio="none">
      <defs>
        <linearGradient id="couple-tone" x1="0" y1="0" x2="1" y2="1">
          <stop offset="0" stop-color="var(--navy)"/>
          <stop offset="1" stop-color="var(--navy-deep)"/>
        </linearGradient>
        <linearGradient id="advisor-tone" x1="0" y1="0" x2="1" y2="0">
          <stop offset="0" stop-color="var(--brick)"/>
          <stop offset="0.55" stop-color="var(--brick-light)"/>
          <stop offset="1" stop-color="#efeae4"/>
        </linearGradient>
      </defs>
      <polygon role="img" aria-label="Photo of a smiling retired couple, tinted navy"
               points="770,0 1545,0 1200,412" fill="url(#couple-tone)"/>
      <polygon role="img" aria-label="Portrait photo of the advisor in a white polo shirt in front of a brick wall"
               points="1545,0 1760,0 1760,512 1410,512 1250,370" fill="url(#advisor-tone)"/>
      <polygon class="wedge" points="1120,512 1250,370 1410,512" fill="var(--grey-wedge)"/>
    </svg>

    <div class="brand">
      <span class="brand-square"></span>
      <span class="brand-name">GRANITE BRIDGE FINANCIAL</span>
    </div>

    <h1 class="headline">Financial freedom<br>is not a myth</h1>
    <div class="headline-rule"></div>

    <ul class="services">
      <li>Retirement<br>Planning</li>
      <li>College<br>Planning</li>
      <li>Estate<br>Planning</li>
      <li>Helpful<br>Advice</li>
      <li>Many<br>More</li>
    </ul>

    <div class="contact">
      <span class="phone">
        <svg viewBox="0 0 24 24" aria-hidden="true">
          <circle cx="12" cy="12" r="10.5" fill="none" stroke="var(--navy)" stroke-width="1.6"/>
          <path d="M8.2 6.8l1.8-.6 1.3 2.8-1.2 1c.5 1.4 1.5 2.5 2.9 3.1l1-1.2 2.8 1.3-.6 1.8c-.3.8-1.1 1.2-1.9 1-3.4-.9-6-3.5-6.9-6.9-.2-.8.2-1.6.8-2.3z" fill="var(--navy)"/>
        </svg>
        304.555.0142
      </span>
      <span class="web">www.<span class="domain">granitebridgefinancial-example</span>.com</span>
    </div>
  </section>
</body>
</html>
```